Book-my-Mentor-Berlin Club

I would like an envelope that I give to companies or customers in order to draw attention to a birthday, loyalty or celebration. The cover should be based on the homepage / www.book-my-mentor-berlin.example (colors and design).

with sporty greetings, Florian Haberkorn
book my mentor berlin
Kastanien Str. 41
10439 Berlin

```html
<!DOCTYPE html>
<html lang="en">
<head>
<meta charset="utf-8">
<title>Book-my-Mentor-Berlin Club – Greeting Envelope</title>
<link rel="stylesheet" href="https://fonts.googleapis.com/css2?family=Allura&family=Yellowtail&family=Open+Sans:wght@400;700&family=Roboto+Condensed:wght@700&display=swap">
<style>
  :root {
    --backdrop: #cfcfcf;
    --envelope-black: #070808;
    --flap-black: #030404;
    --floor-grey: #6a6a6a;
    --floor-dark: #1e1f20;
    --accent-red: #e0483e;
    --paper-white: #f4f4f4;
    --muted-white: #d8d8d8;
  }
  html, body {
    margin: 0;
    padding: 0;
    width: 1200px;
    height: 880px;
    overflow: hidden;
    background: var(--backdrop);
  }
  .envelope {
    position: absolute;
    left: 100px;
    top: 190px;
    width: 1000px;
    height: 500px;
    background: var(--envelope-black);
    overflow: hidden;
    box-shadow: 0 14px 30px rgba(0,0,0,0.18);
  }
  .envelope__flap {
    position: absolute;
    left: 0;
    top: 0;
    width: 100%;
    height: 44px;
    background: var(--flap-black);
    border-bottom: 1px solid #141515;
    z-index: 3;
  }
  .envelope__photo {
    position: absolute;
    inset: 0;
    background:
      linear-gradient(180deg, var(--envelope-black) 0%, var(--envelope-black) 38%, #2a2b2c 62%, #4e4f50 82%, var(--floor-grey) 100%),
      var(--envelope-black);
    z-index: 1;
  }
  .envelope__photo::after {
    content: "";
    position: absolute;
    inset: 0;
    background: linear-gradient(90deg, rgba(0,0,0,0) 0%, rgba(0,0,0,0) 45%, rgba(0,0,0,0.55) 100%);
  }
  .club-mark {
    position: absolute;
    left: 40px;
    top: 68px;
    display: flex;
    align-items: center;
    gap: 8px;
    z-index: 4;
  }
  .club-mark__dot {
    width: 14px;
    height: 14px;
    border-radius: 50%;
    background: var(--paper-white);
  }
  .club-mark__name {
    font-family: "Open Sans", sans-serif;
    font-weight: 700;
    font-size: 11px;
    letter-spacing: 0.06em;
    color: var(--paper-white);
    text-transform: uppercase;
  }
  .sender {
    position: absolute;
    left: 44px;
    top: 230px;
    z-index: 4;
  }
  .sender__greeting {
    font-family: "Yellowtail", cursive;
    font-size: 24px;
    color: var(--accent-red);
    margin: 0 0 4px 40px;
  }
  .sender__signature {
    font-family: "Allura", cursive;
    font-size: 62px;
    line-height: 1;
    color: var(--paper-white);
    margin: 0 0 8px 0;
  }
  .sender__company {
    font-family: "Roboto Condensed", sans-serif;
    font-weight: 700;
    font-size: 17px;
    color: var(--paper-white);
    text-transform: uppercase;
    margin: 0;
  }
  .sender__address {
    font-family: "Open Sans", sans-serif;
    font-weight: 400;
    font-size: 15px;
    color: var(--muted-white);
    margin: 2px 0 0 0;
  }
</style>
</head>
<body>
  <section class="envelope">
    <div class="envelope__flap"></div>
    <div class="envelope__photo" role="img" aria-label="Dark black-and-white photo of an empty gym with a worn wooden floor fading into darkness"></div>

    <div class="club-mark">
      <span class="club-mark__dot"></span>
      <span class="club-mark__name">Book-my-Mentor-Berlin Club</span>
    </div>

    <div class="sender">
      <p class="sender__greeting">With Sporty Greetings</p>
      <p class="sender__signature">Florian Haberkorn</p>
      <p class="sender__company">Book my mentor berlin</p>
      <p class="sender__address">Kastanien Str. 41 10439 Berlin</p>
    </div>
  </section>
</body>
</html>
```